Real Estate Company Looking for Business Card Designs for 3 Executives

Hello!
Thanks so much for considering our project! We are a real estate investment company located in Edmonton, Alberta called Bellcrane Group of Companies. We invest/develop both commercial and residential real estate and are looking to create 3 DOUBLE-SIDED business cards for 3 top executives in the company! (for some reason it won't let us select the double-sided option, but yes, the cards are double sided and would be happy to tip extra)

We have certain guidelines that we want our business cards to for sure follow - the back of the Business card has to be the Black Background Version of the Logo which has already been designed and linked as a file (first file). We want the entire back of the card to simply just be the black background logo. In terms of the front of the card, would like to see a smaller version of the white background logo (linked as the second file) in the top left hand corner - of course, feel free to get creative and we can make revisions together along the way! and Then after that, just text. We want the card to be sharp, clean, easy on the eyes and highly professional looking. We would like the card to include the Full name of the Company (Bellcrane Group of Companies), Name of the Person, Title, Phone, Email. If possible please provide the front part of the card for 3 people:

1) Bellcrane Group of Companies, Nora Lindqvist, Chief Financial Officer, 780-555-0142, noralindqvist@bellcranegroup.example

2) Bellcrane Group of Companies, Julien Lindqvist, Chief Executive Officer, 780-555-0187, julienlindqvist@bellcranegroup.example

3) Bellcrane Group of Companies, Tom Okafor, Chief Operations Officer, 587-555-0163, tomokafor@bellcranegroup.example

Thank you so much for considering our project & we look forward to seeing your designs!

```html
<!DOCTYPE html>
<html lang="en">
<head>
<meta charset="utf-8">
<title>Bellcrane Business Card – Front</title>
<link href="https://fonts.googleapis.com/css2?family=Karla:wght@400;500;700&display=swap" rel="stylesheet">
<style>
  :root {
    --page-bg: #d9d6d1;
    --card-bg: #f3f2ef;
    --ink: #1b1b1b;
    --ink-soft: #3a3a3a;
    --tree-dark: #161616;
    --tree-light: #4a4a4a;
  }
  html, body {
    margin: 0;
    width: 1200px;
    height: 969px;
    overflow: hidden;
    background: var(--page-bg);
    font-family: "Karla", sans-serif;
  }
  .card {
    position: absolute;
    left: 75px;
    top: 184px;
    width: 1050px;
    height: 600px;
    background: var(--card-bg);
    border-radius: 26px;
    overflow: hidden;
    box-shadow: 0 4px 18px rgba(0,0,0,0.12);
    color: var(--ink);
  }
  .brand {
    position: absolute;
    left: 92px;
    top: 220px;
    margin: 0;
    font-size: 30px;
    font-weight: 500;
    letter-spacing: 9px;
    color: var(--ink);
  }
  .accent-bar {
    position: absolute;
    left: 0;
    top: 341px;
    width: 15px;
    height: 74px;
    background: var(--ink);
  }
  .person-name {
    position: absolute;
    left: 90px;
    top: 338px;
    margin: 0;
    font-size: 35px;
    font-weight: 700;
    letter-spacing: 0.5px;
  }
  .person-title {
    position: absolute;
    left: 91px;
    top: 384px;
    margin: 0;
    font-size: 20px;
    font-weight: 400;
    color: var(--ink-soft);
  }
  .contact-list {
    position: absolute;
    left: 92px;
    top: 438px;
    margin: 0;
    padding: 0;
    list-style: none;
    font-size: 21px;
    color: var(--ink-soft);
  }
  .contact-list li {
    display: flex;
    align-items: center;
    height: 29px;
  }
  .contact-list svg {
    width: 18px;
    height: 18px;
    margin-right: 10px;
    flex: none;
  }
  .tree-art {
    position: absolute;
    left: 735px;
    top: 0;
    width: 225px;
    height: 600px;
    background: linear-gradient(90deg, var(--tree-light) 0%, var(--tree-dark) 40%, var(--tree-light) 100%);
    opacity: 0.9;
  }
</style>
</head>
<body>
  <section class="card">
    <p class="brand">BELLCRANE</p>

    <div class="accent-bar"></div>
    <h1 class="person-name">NORA LINDQVIST</h1>
    <p class="person-title">Chief Financial Officer</p>

    <ul class="contact-list">
      <li>
        <svg viewBox="0 0 24 24" fill="none" stroke="currentColor" stroke-width="2" stroke-linecap="round" stroke-linejoin="round"><path d="M22 16.9v3a2 2 0 0 1-2.2 2 19.8 19.8 0 0 1-8.6-3.1 19.5 19.5 0 0 1-6-6A19.8 19.8 0 0 1 2.1 4.2 2 2 0 0 1 4.1 2h3a2 2 0 0 1 2 1.7c.1 1 .4 1.9.7 2.8a2 2 0 0 1-.5 2.1L8 9.8a16 16 0 0 0 6 6l1.3-1.3a2 2 0 0 1 2.1-.4c.9.3 1.8.6 2.8.7a2 2 0 0 1 1.7 2z"/></svg>
        780-555-0142
      </li>
      <li>
        <svg viewBox="0 0 24 24" fill="none" stroke="currentColor" stroke-width="2" stroke-linejoin="round"><rect x="3" y="5" width="18" height="14" rx="1"/><path d="M3 6l9 7 9-7"/></svg>
        noralindqvist@bellcranegroup.example
      </li>
      <li>
        <svg viewBox="0 0 24 24" fill="currentColor"><circle cx="12" cy="12" r="10"/></svg>
        bellcranegroup.example
      </li>
    </ul>

    <div class="tree-art" role="img" aria-label="Illustration of two tall conifer tree silhouettes in black"></div>
  </section>
</body>
</html>
```